Innovative Funky Australian Start Up - HR & Recruitment

We would like a brochure for our company "Crew Harbor". We provide affordable HR & Recruitment support for Small to Medium businesses.
We like a simple, fresh, crisp, clean look. Nothing overly complicated.
Target market is Small and medium businesses with 2-50 employees, this could be in IT, Accounting, Construction, Marketing or a Engineering, so really trying to appeal to all industries. We don’t want to come across as too high end corporate – more everyday professional. I’d say our target client is probably late 30’s to late 40’s owner or general manager
Our website is - www.crewharbor-example.com.au

Target Market(s)

Small and medium size business's.
Business owners.
Multiple industries

Industry/Entity Type

It Company

Font styles to use
Sans Serif

```html
<!DOCTYPE html>
<html lang="en">
<head>
<meta charset="utf-8">
<title>Crew Harbor – HR Services Brochure Spread</title>
<link rel="stylesheet" href="https://fonts.googleapis.com/css2?family=Jost:wght@400;500&display=swap">
<style>
  :root {
    --navy: #2b5486;
    --navy-deep: #244a78;
    --sky: #3f8fd8;
    --paper: #ffffff;
    --backdrop: #e4e6ea;
    --text-light: #eef3fa;
    --photo-office: #c9d3de;
    --photo-office-2: #e8ecf0;
    --photo-meeting: #d8d0c6;
    --photo-meeting-2: #f1ede7;
    --bullet: #e24a4a;
  }
  * { box-sizing: border-box; margin: 0; padding: 0; }
  html, body { width: 1200px; height: 789px; overflow: hidden; }
  body {
    background: var(--backdrop);
    font-family: "Jost", "Futura", sans-serif;
    color: var(--text-light);
  }
  .spread {
    position: absolute;
    left: 77px; top: 24px;
    width: 1046px; height: 740px;
    display: flex;
    box-shadow: 0 10px 30px rgba(0,0,0,.18);
  }
  .page {
    position: relative;
    width: 523px; height: 740px;
    background: var(--paper);
    overflow: hidden;
  }
  .page-shapes { position: absolute; inset: 0; width: 100%; height: 100%; }
  .photo { position: absolute; left: 0; width: 100%; }
  .photo-office {
    top: 0; height: 420px;
    background: linear-gradient(135deg, var(--photo-office-2), var(--photo-office) 70%, #9aa6b4);
  }
  .photo-meeting {
    top: 320px; height: 420px;
    background: linear-gradient(160deg, var(--photo-meeting-2), var(--photo-meeting) 60%, #b9c3cf);
  }

  /* Left page text */
  .services-title {
    position: absolute; right: 34px; top: 455px;
    font-size: 30px; font-weight: 400; letter-spacing: 1px;
    text-transform: uppercase;
  }
  .services-copy {
    position: absolute; left: 34px; right: 34px; top: 510px;
    font-size: 10.5px; line-height: 1.45;
  }
  .services-copy p { margin-bottom: 9px; }

  /* Right page text */
  .assist-title {
    position: absolute; left: 40px; top: 30px;
    font-size: 21px; font-weight: 400; letter-spacing: .5px;
    text-transform: uppercase;
  }
  .assist-list {
    position: absolute; list-style: none;
    font-size: 10px; line-height: 1.75;
  }
  .assist-list.primary { left: 40px; top: 72px; }
  .assist-list.secondary { left: 300px; top: 180px; }
  .assist-list li { display: flex; align-items: center; gap: 7px; }
  .assist-list .gap { margin-top: 10px; }
  .bullet {
    width: 8px; height: 8px; border-radius: 50%;
    background: var(--paper); border: 2px solid var(--bullet);
    flex: none;
  }
</style>
</head>
<body>
  <main class="spread">
    <section class="page page-left">
      <div class="photo photo-office" role="img" aria-label="Photo of a smiling businesswoman in a blazer with colleagues at a meeting table behind her"></div>
      <svg class="page-shapes" viewBox="0 0 523 740" aria-hidden="true">
        <path d="M0,285 L330,392 L0,398 Z" fill="var(--sky)"/>
        <path d="M0,395 Q260,378 523,402 L523,740 L0,740 Z" fill="var(--navy)"/>
      </svg>
      <h1 class="services-title">HR Services</h1>
      <div class="services-copy">
        <p>Retained, Outsourced HR. Let us be your dedicated, regular HR support, whether that's for two days a week or two hours a month. We're there as you need us in person or over the phone. We offer monthly memberships and regular internal &amp; external support at reduced rates.</p>
        <p>HR Consulting. Whether it's workplace investigations, dismissal or remuneration &amp; benefits advice, performance management, manager training or working with your business to build high performance teams, we have an option to suit your business.</p>
        <p>Onsite Support. Our experienced HR &amp; Recruitment Consultants are available for onsite support for project delivery, peak workloads, recruitment campaigns and restructures.</p>
        <p>HR for SME's &amp; Start-Ups. We provide you with all the HR Documentation that your business needs, so you can be confident that you are meeting your legal requirements. This includes employment contracts, policies &amp; procedures, new employee forms, induction checklists &amp; more.</p>
      </div>
    </section>

    <section class="page page-right">
      <div class="photo photo-meeting" role="img" aria-label="Photo of a man presenting at a whiteboard to colleagues seated around a table with laptops"></div>
      <svg class="page-shapes" viewBox="0 0 523 740" aria-hidden="true">
        <path d="M0,0 H523 V300 Q260,315 0,335 Z" fill="var(--navy)"/>
        <path d="M0,185 L200,330 L0,336 Z" fill="var(--sky)"/>
      </svg>
      <h2 class="assist-title">We assist clients with:</h2>
      <ul class="assist-list primary">
        <li><span class="bullet"></span>Review of employment contracts</li>
        <li><span class="bullet"></span>Workplace investigations including bullying and misconduct</li>
        <li><span class="bullet"></span>Managing people related issues or aggrieved employees</li>
        <li><span class="bullet"></span>Disciplinary advice and procedures</li>
        <li><span class="bullet"></span>FairWork and unfair dismissal assistance</li>
        <li><span class="bullet"></span>Staff Training &amp; Induction processes</li>
        <li><span class="bullet"></span>Creation of Performance Management programs</li>
        <li><span class="bullet"></span>Performance improvement procedures</li>
        <li><span class="bullet"></span>Talent Acquisition &amp; Employee Retention</li>
      </ul>
      <ul class="assist-list secondary">
        <li><span class="bullet"></span>Termination or Redundancy advice</li>
        <li><span class="bullet"></span>Creation of Job descriptions</li>
        <li><span class="bullet"></span>Interview Techniques for Managers</li>
        <li class="gap"><span class="bullet"></span>Remuneration &amp; Benefits Advice</li>
        <li><span class="bullet"></span>Managing Organisational Change</li>
      </ul>
    </section>
  </main>
</body>
</html>
```